Residential improvers, A Quiet Harbor 9 Me *

Quiet Harbor 9 Me is a real estate company specializing in turning unloved properties into improved, happy places to live. We specialize in thoughtfully-improved residential properties for buyers or renters. Our company needs a business card that reflects the renovated homes we create using green and Feng Shui principles,

Please disregard the images we submitted. We are looking for an abstract, sophisticated elegant design. No eggs in a nest ... nothing cute. The image can be soft.
Updates

Aloha (hello) all designers. We are a serious property investment/improvement company. We strive to be unique, renovating with style and elegance. Our business card must portray the same message. We thought the nest and flower might be "it" ... clearly it's not, once we saw what you submitted. Please revisit the brief as it was modified yesterday. Mahalo for your input! We look forward to hearing from all designers that have been invited.

Industry/Entity Type

Real Estate Development

Contact Information for Business Card

We will have separate business cards for
1) Corabeth Danvers 808-555-0173 corabeth@mailtrove.net
2) Trina Vasquell 808-555-0196 trinavasquell@mailtrove.net
** can we add the website later ... in the process of approval.
Investors * Renovators * Connectors

Font styles to use
Sans Serif

Colors
cadf82

Requirements
Must have
• a feng shui feel ... modern. Color - green with black print.
Nice to have
• A Quiet Harbor 9 Me

```html
<!DOCTYPE html>
<html lang="en">
<head>
<meta charset="UTF-8">
<title>A Quiet Harbor 9 Me — Business Card</title>
<link rel="stylesheet" href="https://fonts.googleapis.com/css2?family=Lato:wght@300;400&display=swap">
<style>
  :root {
    --green: #a9bd62;
    --green-line: #b8c97a;
    --black: #141414;
    --white: #ffffff;
    --ink: #1a1a1a;
    --stage: #e9ebe6;
  }
  * { margin: 0; padding: 0; box-sizing: border-box; }
  html, body { width: 1200px; height: 900px; overflow: hidden; }
  body {
    background: var(--stage);
    font-family: 'Lato', sans-serif;
    display: flex;
    flex-direction: column;
    align-items: center;
    justify-content: center;
    gap: 60px;
  }
  .card {
    width: 630px;
    height: 360px;
    position: relative;
    box-shadow: 0 6px 18px rgba(0,0,0,0.18);
    overflow: hidden;
  }

  /* Front */
  .card-front { background: var(--white); }
  .front-brand {
    position: absolute;
    left: 48px;
    top: 70px;
    display: flex;
    align-items: center;
    gap: 12px;
  }
  .brand-square {
    width: 14px;
    height: 14px;
    background: var(--green);
  }
  .front-brand .brand-name {
    font-weight: 300;
    font-size: 28px;
    color: var(--ink);
    letter-spacing: -0.3px;
  }
  .divider {
    position: absolute;
    left: 330px;
    top: 52px;
    width: 1.5px;
    height: 165px;
    background: var(--green-line);
  }
  .contact {
    position: absolute;
    left: 358px;
    top: 78px;
    color: var(--ink);
  }
  .contact-name {
    font-size: 26px;
    font-weight: 400;
    margin-bottom: 14px;
  }
  .contact-row {
    display: flex;
    align-items: center;
    gap: 10px;
    font-size: 18px;
    margin-bottom: 6px;
  }
  .contact-row svg { width: 16px; height: 16px; fill: var(--green); flex: none; }
  .web-band {
    position: absolute;
    left: 0; right: 0; bottom: 0;
    height: 92px;
    background: var(--green);
    display: flex;
    align-items: center;
    padding-left: 48px;
  }
  .web-band span {
    color: var(--white);
    font-size: 18px;
    letter-spacing: 3px;
  }

  /* Back */
  .card-back {
    background: var(--black);
    display: flex;
    flex-direction: column;
    align-items: center;
    justify-content: center;
  }
  .back-brand {
    display: flex;
    align-items: center;
    gap: 16px;
    margin-bottom: 28px;
  }
  .back-brand .brand-square { width: 18px; height: 18px; }
  .back-brand .brand-name {
    font-weight: 300;
    font-size: 44px;
    color: var(--white);
    letter-spacing: -0.5px;
  }
  .tagline {
    color: var(--green);
    font-size: 16px;
    letter-spacing: 0.8px;
    word-spacing: 6px;
  }
</style>
</head>
<body>
  <section class="card card-front">
    <div class="front-brand">
      <span class="brand-square"></span>
      <span class="brand-name">A Quiet Harbor 9 Me</span>
    </div>
    <div class="divider"></div>
    <div class="contact">
      <p class="contact-name">Corabeth Danvers</p>
      <p class="contact-row">
        <svg viewBox="0 0 24 24" aria-hidden="true"><path d="M6.6 10.8a15.1 15.1 0 0 0 6.6 6.6l2.2-2.2a1 1 0 0 1 1-.25 11.4 11.4 0 0 0 3.6.57 1 1 0 0 1 1 1V20a1 1 0 0 1-1 1A17 17 0 0 1 3 4a1 1 0 0 1 1-1h3.5a1 1 0 0 1 1 1c0 1.25.2 2.45.57 3.57a1 1 0 0 1-.25 1z"/></svg>
        808-555-0173
      </p>
      <p class="contact-row">
        <svg viewBox="0 0 24 24" aria-hidden="true"><path d="M2 5h20v14H2z M3.5 6.5 12 13l8.5-6.5" fill="var(--green)"/><path d="M3 6l9 7 9-7" fill="none" stroke="#fff" stroke-width="1.5"/></svg>
        corabeth@mailtrove.net
      </p>
    </div>
    <div class="web-band"><span>www.aquietharbor9me.com</span></div>
  </section>

  <section class="card card-back">
    <div class="back-brand">
      <span class="brand-square"></span>
      <span class="brand-name">A Quiet Harbor 9 Me</span>
    </div>
    <p class="tagline">Investors | Renovators | Connectors</p>
  </section>
</body>
</html>
```